Monthly Wall Calendar for Brinvale Paws Rescue

We will provide photo's description of dogs and placement of photos and all written material for calendar. We need a wall calendar and we will need as a final output pdf files with the proper bleed lines to send to printer. We have uploaded what the prior year calendar looked like. We are looking for something similar this year.

Generally there is a large monthly photo and 2-3 smaller ones added to the calendar page.

Target Market(s)

Our supporters and animal rescue people.

Font styles to use
Serif

Colors
6c459b
b7a5cd

Requirements
Must have
• A final pdf file with bleed lines for printer.
Nice to have
• The uploaded calendar gives a nice idea of what we are looking for as well as this link. http://brinvalepaws.com/calendar-2016-photo-spread/ and http://brinvalepaws.com/covers-2017/
Should not have
• Not cluttered

```html
<!DOCTYPE html>
<html lang="en">
<head>
<meta charset="utf-8">
<title>Brinvale Paws Rescue — January Wall Calendar</title>
<link href="https://fonts.googleapis.com/css2?family=Anton&family=Roboto+Condensed:wght@300;400;700&display=swap" rel="stylesheet">
<style>
  :root {
    --purple: #6c459b;
    --purple-soft: #7d5cc0;
    --lavender: #b7a5cd;
    --backdrop: #d2d0f7;
    --paper: #ffffff;
    --grid-line: #c9bde0;
  }
  * { margin: 0; padding: 0; box-sizing: border-box; }
  html, body { width: 1200px; height: 1200px; overflow: hidden; }
  body { background: var(--backdrop); font-family: "Roboto Condensed", sans-serif; position: relative; }

  .calendar-page {
    position: absolute; left: 233px; top: 29px;
    width: 923px; height: 1437px;
    background: var(--paper);
    transform: scale(0.8); transform-origin: 0 0;
  }

  .hero-photo {
    position: absolute; left: 0; top: 0; width: 923px; height: 711px;
    background:
      radial-gradient(ellipse at 78% 55%, #6b4a2a 0%, #3d2c1c 28%, transparent 52%),
      radial-gradient(ellipse at 30% 40%, #8fae3c 0%, #5f8a22 45%, #3f6416 100%);
  }
  .intro-panel {
    position: absolute; left: 65px; top: 0; width: 337px; height: 560px;
    background: rgba(190, 215, 140, 0.45);
  }
  .intro-text {
    position: absolute; left: 111px; top: 104px; width: 252px;
    font-size: 14px; line-height: 21px; color: #1d2412; font-weight: 400;
    letter-spacing: -0.45px;
  }
  .month-title {
    position: absolute; left: 42px; top: 566px;
    font-family: "Anton", sans-serif; font-size: 126px; line-height: 1;
    font-weight: 400; color: var(--lavender); letter-spacing: 0;
    transform: scaleX(0.85); transform-origin: 0 0; white-space: nowrap;
  }
  .photo-caption {
    position: absolute; left: 790px; top: 638px;
    font-size: 10px; line-height: 14px; font-weight: 700;
    color: #fff; letter-spacing: 1px; text-transform: uppercase;
  }

  .weekday-row {
    position: absolute; left: 9px; top: 735px; width: 908px;
    display: grid; grid-template-columns: repeat(7, 1fr);
    border-bottom: 2px solid var(--lavender); padding-bottom: 6px;
  }
  .weekday-row span {
    text-align: center; font-size: 14px; font-weight: 700;
    color: var(--purple-soft); text-transform: uppercase;
  }

  .month-grid {
    position: absolute; left: 27px; top: 762px; width: 871px;
    display: grid; grid-template-columns: 118px repeat(6, 127px);
    grid-auto-rows: 102px;
  }
  .day {
    position: relative; border-bottom: 1px solid var(--grid-line);
    border-left: 2px solid var(--grid-line);
  }
  .day:nth-child(7n+1) { border-left: none; }
  .month-grid .day:nth-last-child(-n+7) { border-bottom: none; }
  .day-number {
    position: absolute; right: 9px; top: 6px;
    font-size: 11px; color: var(--purple);
  }
  .holiday {
    position: absolute; right: 9px; top: 22px; width: 70px; text-align: right;
    font-size: 7px; line-height: 11px; color: var(--purple-soft);
  }

  .thumb-photo { position: absolute; top: 1292px; height: 140px; }
  .thumb-resting { left: 0; width: 198px; background: linear-gradient(135deg, #4a3322, #8a5a30 55%, #2b1c12); }
  .thumb-standing { left: 387px; width: 225px; background: linear-gradient(180deg, #7fb2e8 0%, #a9cdee 60%, #b8a98a 100%); }
  .footer-text {
    position: absolute; left: 224px; top: 1294px; width: 142px;
    font-size: 10px; line-height: 13.7px; color: var(--purple-soft); letter-spacing: -0.4px;
  }

  .mini-month { position: absolute; top: 1288px; width: 122px; color: var(--purple-soft); }
  .mini-month.december { left: 633px; }
  .mini-month.february { left: 779px; }
  .mini-month h3 { font-size: 10px; font-weight: 700; text-align: center; margin-bottom: 3px; }
  .mini-days { display: grid; grid-template-columns: repeat(7, 1fr); font-size: 9px; line-height: 15px; text-align: center; font-weight: 300; }
  .mini-days .small { font-size: 6px; line-height: 15px; }
</style>
</head>
<body>
<main class="calendar-page">
  <div class="hero-photo" role="img" aria-label="Close-up photograph of a German shepherd panting, against a soft green leafy background"></div>
  <div class="intro-panel"></div>
  <p class="intro-text">Ipicim eatus et adicius andandaecto to tem dolorep udantempor autem iundis dolo officat iustrum et reribus, untur?<br>Occatus. Am latempos etur alitat minus. Lectioris dis eum hario minitaq uation cone dignatur aditatem velia saecaecto mi, quam, consedi gnihit quiberu mquasperum idignimin cus magnam unti dis andus, cullum hariamus, sam, tes es qui offictotatem evendit offic temo consedi genimil itemporenem iumquid quossit officium faccaep eribus nonse veliatument.<br>Qui re dus sitaspedis rent et dolore sus, ellam, nobis aboribus verovit ibusapidem ipsam reptate pa volum es arci cusae pa vid quaspe qundis adi suntiam cum quat rehenis aut ea none liquos delendel is repeliquam, alicietum enet quibusdam voluptat fugitem porero offic to blant laut plat alicaecto dolorio in cus a dese vendant quat asitios nam nullandam quam, sam labo. Ut</p>
  <h1 class="month-title">JANUARY</h1>
  <p class="photo-caption">Xim audant licaborro<br>volut hil et rerum<br>necae sanduci ligenih</p>

  <div class="weekday-row">
    <span>Sunday</span><span>Monday</span><span>Tuesday</span><span>Wednesday</span><span>Thursday</span><span>Friday</span><span>Saturday</span>
  </div>

  <section class="month-grid">
    <div class="day"></div>
    <div class="day"><span class="day-number">1</span><span class="holiday">New Year's Day</span></div>
    <div class="day"><span class="day-number">2</span></div>
    <div class="day"><span class="day-number">3</span></div>
    <div class="day"><span class="day-number">4</span></div>
    <div class="day"><span class="day-number">5</span></div>
    <div class="day"><span class="day-number">6</span></div>
    <div class="day"><span class="day-number">7</span></div>
    <div class="day"><span class="day-number">8</span></div>
    <div class="day"><span class="day-number">9</span></div>
    <div class="day"><span class="day-number">10</span></div>
    <div class="day"><span class="day-number">11</span></div>
    <div class="day"><span class="day-number">12</span></div>
    <div class="day"><span class="day-number">13</span></div>
    <div class="day"><span class="day-number">14</span></div>
    <div class="day"><span class="day-number">15</span><span class="holiday">Community<br>Service Day</span></div>
    <div class="day"><span class="day-number">16</span></div>
    <div class="day"><span class="day-number">17</span></div>
    <div class="day"><span class="day-number">18</span></div>
    <div class="day"><span class="day-number">19</span></div>
    <div class="day"><span class="day-number">20</span></div>
    <div class="day"><span class="day-number">21</span></div>
    <div class="day"><span class="day-number">22</span></div>
    <div class="day"><span class="day-number">23</span></div>
    <div class="day"><span class="day-number">24</span></div>
    <div class="day"><span class="day-number">25</span></div>
    <div class="day"><span class="day-number">26</span></div>
    <div class="day"><span class="day-number">27</span></div>
    <div class="day"><span class="day-number">28</span></div>
    <div class="day"><span class="day-number">29</span></div>
    <div class="day"><span class="day-number">30</span></div>
    <div class="day"><span class="day-number">31</span></div>
    <div class="day"></div>
    <div class="day"></div>
    <div class="day"></div>
  </section>

  <div class="thumb-photo thumb-resting" role="img" aria-label="Photograph of a German shepherd lying down, resting its head on its paws"></div>
  <p class="footer-text">Cone porro volum volore, ellabor erepeli quibus vendaest apit, quunt quate vendae omnihiti volupta tiatur mo doluptas dolluptia ipsusda epellictur, odipsus quo escieniam re estibus alitatia pero tem ad ullaut ommolo blaut volo vit ut aut expliquides simenie necabor</p>
  <div class="thumb-photo thumb-standing" role="img" aria-label="Photograph of a German shepherd standing on a rock under a blue sky"></div>

  <section class="mini-month december">
    <h3>December 2017</h3>
    <div class="mini-days">
      <span>S</span><span>M</span><span>T</span><span>W</span><span>T</span><span>F</span><span>S</span>
      <span></span><span></span><span></span><span></span><span></span><span>1</span><span>2</span>
      <span>3</span><span>4</span><span>5</span><span>6</span><span>7</span><span>8</span><span>9</span>
      <span>10</span><span>11</span><span>12</span><span>13</span><span>14</span><span>15</span><span>16</span>
      <span>17</span><span>18</span><span>19</span><span>20</span><span>21</span><span>22</span><span>23</span>
      <span class="small">24/31</span><span>25</span><span>26</span><span>27</span><span>28</span><span>29</span><span>30</span>
    </div>
  </section>
  <section class="mini-month february">
    <h3>February 2018</h3>
    <div class="mini-days">
      <span>S</span><span>M</span><span>T</span><span>W</span><span>T</span><span>F</span><span>S</span>
      <span></span><span></span><span></span><span></span><span>1</span><span>2</span><span>3</span>
      <span>4</span><span>5</span><span>6</span><span>7</span><span>8</span><span>9</span><span>10</span>
      <span>11</span><span>12</span><span>13</span><span>14</span><span>15</span><span>16</span><span>17</span>
      <span>18</span><span>19</span><span>20</span><span>21</span><span>22</span><span>23</span><span>24</span>
      <span>25</span><span>26</span><span>27</span><span>28</span><span></span><span></span><span></span>
    </div>
  </section>
</main>
</body>
</html>
```